RivoPlex PowerPoint Template with existing Logo and Letterhead template

Develop a PowerPoint template based on existing logo and letterhead designs for a Marketing Consultancy.
Presentations that will be made with title slide, content slides (which includes mostly bullet point text and some tables) and also last page company introduction and copyright.
Corporate colors should be keep as per the logo

I like something like from Artisan Hive
- Serious, Modern PowerPoint Design for Company in Canada | Design 418674
- Professional, Modern PowerPoint Design for Company in United States | Design 7795293
- Professional, Modern PowerPoint Design for Company in United States | Design 7826742
- Serious, Modern PowerPoint Design for Company in Canada | Design 418635
- Elegant, Serious PowerPoint Design for Company in Puerto Rico | Design 16951178
- Bold, Modern PowerPoint Design for Company in United States | Design 11745238

To all designers, • We need sleek and modern looking PowerPoint presentation template. • The template will primarily be used for our corporate slide and solutions presentation for our customers. • Not too much of white and it should be sleek, modern and impressive for marketing consultancy firms like us. • Please ensure the content pages are water marketed with the 4 boxes. • I like something like from Artisan Hive and you can get some idea on what I like.: o Serious, Modern PowerPoint Design for Company in Canada | Design 418674 o Professional, Modern PowerPoint Design for Company in United States | Design 7795293 o Professional, Modern PowerPoint Design for Company in United States | Design 7826742 o Serious, Modern PowerPoint Design for Company in Canada | Design 418635 o Elegant, Serious PowerPoint Design for Company in Puerto Rico | Design 16951178 o Bold, Modern PowerPoint Design for Company in United States | Design 11745238 Thanks!

Target Market(s)

Marketing Managers, B2B Marketing Team, CRM Data Owners

Industry/Entity Type

Marketing

Requirements
Must have
• Not too much of white and it should be sleek, modern and impressive for marketing consultancy firms like us. Please ensure the content pages are water marketed with the 4 boxes. The template will primarily be used for our corporate slides and solutions presentation for our customers.
Should not have
• no background in the slide content area

```html
<!DOCTYPE html>
<html lang="en">
<head>
<meta charset="utf-8">
<title>RivoPlex Presentation Template</title>
<link href="https://fonts.googleapis.com/css2?family=Oswald:wght@400;500;600&family=Open+Sans:wght@400;600&display=swap" rel="stylesheet">
<style>
:root{
  --stage:#2e2e2e;
  --red:#e31e26;
  --slate:#4b5261;
  --green:#5e9a3b;
  --purple:#7b2682;
  --ink:#3a3a3a;
  --mute:#8a8a8a;
  --line:#d9d9d9;
  --panel:#efefef;
  --white:#ffffff;
  --sky:linear-gradient(180deg,#5d86b8 0%,#8fb0cf 45%,#c9a684 80%,#5a6b82 100%);
  --night:linear-gradient(180deg,#1f3f7a 0%,#3567a8 50%,#d79a52 85%,#263248 100%);
  --dusk:linear-gradient(180deg,#6a86a8 0%,#b6c2cc 50%,#9a8a78 80%,#3c4452 100%);
}
*{box-sizing:border-box;margin:0;padding:0}
html,body{width:1200px;height:595px;overflow:hidden;background:var(--stage)}
body{position:relative;font-family:"Open Sans",Arial,sans-serif;color:var(--ink)}
.slide{position:absolute;width:190px;height:104px;background:var(--white);overflow:hidden}
.photo{position:absolute;background:var(--sky)}
.photo.night{background:var(--night)}
.photo.dusk{background:var(--dusk)}
.abs{position:absolute}
.tag{position:absolute;left:7px;top:4px;font:600 3.6px "Open Sans",sans-serif;color:var(--mute);text-transform:uppercase;letter-spacing:.1px;border-bottom:.5px solid var(--line);padding-bottom:1px;width:70px;white-space:nowrap}
.mark{position:absolute;right:7px;top:3px;display:flex;align-items:center;gap:1.5px;font:600 6px "Oswald",sans-serif;color:var(--red);letter-spacing:.3px}
.mark i{display:block;width:3px;height:3px;background:var(--red)}
.mark.white{color:var(--white)}
.mark.white i{background:var(--white)}
.pg{position:absolute;right:7px;bottom:4px;width:5px;height:3px;background:var(--slate)}
.hl{position:absolute;font:500 8px "Oswald",sans-serif;color:var(--ink);text-transform:uppercase;line-height:1}
.sub{position:absolute;font:400 3.4px "Open Sans",sans-serif;color:var(--mute);text-transform:uppercase}
.txt{position:absolute;font:400 3.3px/1.35 "Open Sans",sans-serif;color:var(--mute)}
.lbl{position:absolute;font:600 3.6px "Oswald",sans-serif;color:var(--red);text-transform:uppercase}
.bul{position:absolute;display:flex;gap:3px;align-items:flex-start;font:400 3.2px/1.3 "Open Sans",sans-serif;color:var(--mute);width:62px}
.bul b{flex:none;width:4px;height:4px;border:.6px solid var(--red);border-radius:50%}
.dot{position:absolute;border-radius:50%}
.ring{position:absolute;border-radius:50%;border:4px solid}
.band-title{position:absolute;font:500 8px/1.2 "Oswald",sans-serif;color:var(--white);text-transform:uppercase}
.arrow-c{position:absolute;width:11px;height:11px;border:.8px solid var(--white);border-radius:50%}
.arrow-c::after{content:"";position:absolute;left:3px;top:3.2px;width:3px;height:3px;border-top:.8px solid var(--white);border-right:.8px solid var(--white);transform:rotate(45deg)}
.red{background:var(--red)}.slate{background:var(--slate)}.green{background:var(--green)}.purple{background:var(--purple)}
.c-red{border-color:var(--red)}.c-slate{border-color:var(--slate)}.c-green{border-color:var(--green)}.c-purple{border-color:var(--purple)}
.ic{position:absolute;border-radius:50%;}
.ic::after{content:"";position:absolute;left:30%;top:30%;width:40%;height:40%;border:.7px solid var(--white);border-radius:50%}
.ic.o::after{border-color:var(--red)}
table.data{position:absolute;border-collapse:collapse;font:400 2.6px "Open Sans",sans-serif;color:var(--mute)}
table.data th{background:var(--red);color:var(--white);font-weight:600;padding:.8px 1.5px}
table.data td{padding:.8px 1.5px;border-bottom:.3px solid var(--line)}
table.data tr.total td{background:var(--red);color:var(--white)}
/* hero */
.hero{left:11px;top:16px;width:383px;height:215px}
.hero .band{position:absolute;left:0;top:140px;width:191px;height:75px;background:var(--red)}
.hero-title{position:absolute;left:14px;top:18px;font:500 15px "Oswald",sans-serif;color:var(--white)}
.hero-copy{position:absolute;left:30px;top:40px;font:400 5.3px/1.35 "Open Sans",sans-serif;color:var(--white);width:160px}
.hero-mark{position:absolute;left:222px;top:158px;display:flex;align-items:center;gap:4px;font:600 30px "Oswald",sans-serif;color:var(--red);letter-spacing:1px}
.hero-mark i{display:block;width:12px;height:12px;background:var(--red)}
/* closing */
.close{left:800px;top:360px;width:387px;height:216px}
.close-mark{position:absolute;left:118px;top:38px;display:flex;align-items:center;gap:4px;font:600 28px "Oswald",sans-serif;color:var(--white);letter-spacing:1px}
.close-mark i{display:block;width:10px;height:10px;background:var(--white)}
.close .foot{position:absolute;left:0;top:128px;width:387px;height:88px;background:var(--red);color:var(--white)}
.foot h2{position:absolute;font:500 11px "Oswald",sans-serif}
.foot p{position:absolute;left:28px;top:30px;width:230px;font:400 5.2px/1.4 "Open Sans",sans-serif}
.contact{position:absolute;left:288px;top:30px;font:400 5px/1.9 "Open Sans",sans-serif}
.social{position:absolute;left:288px;top:74px;display:flex;gap:4px}
.social span{width:8px;height:8px;border:.7px solid var(--white);border-radius:50%}
</style>
</head>
<body>

<!-- Title slide -->
<section class="slide hero">
  <div class="photo day" style="left:0;top:0;width:191px;height:72px" role="img" aria-label="Daytime city skyline photograph"></div>
  <div class="photo night" style="left:191px;top:0;width:192px;height:72px" role="img" aria-label="Downtown skyline at dusk photograph"></div>
  <div class="photo night" style="left:0;top:72px;width:191px;height:68px" role="img" aria-label="Waterfront museum and skyline at night photograph"></div>
  <div class="photo night" style="left:191px;top:72px;width:192px;height:68px" role="img" aria-label="Twin towers lit at night photograph"></div>
  <div class="band">
    <h1 class="hero-title">HEADLINE HERE</h1>
    <span class="arrow-c" style="left:14px;top:42px"></span>
    <p class="hero-copy">Totatet poruntis que veris sim nonseque pore excoatem as qui dolorep reperibus, officia commihi liquia vellicae consequ ibusti ut num et vent,</p>
  </div>
  <div class="hero-mark"><span>RIVOPLEX</span><i></i></div>
</section>

<!-- Row 1 -->
<section class="slide" style="left:406px;top:16px">
  <div class="photo night" style="left:0;top:0;width:190px;height:104px" role="img" aria-label="Waterfront skyline at night photograph"></div>
  <div class="abs red" style="left:0;top:0;width:96px;height:38px"></div>
  <span class="arrow-c" style="left:6px;top:8px;width:8px;height:8px"></span>
  <p class="band-title" style="left:18px;top:6px;font-size:6px;width:76px">Reach the right people, with the right message, at the right time</p>
  <p class="txt" style="left:6px;top:26px;color:#fff;width:86px">Whether your aim is to acquire new customers, re-engage existing, or grow their value.</p>
  <div class="mark white" style="top:14px"><span>RIVOPLEX</span><i></i></div>
</section>

<section class="slide" style="left:602px;top:16px">
  <span class="tag">Reach the right people, at the right time</span>
  <div class="mark"><span>RIVOPLEX</span><i></i></div>
  <h2 class="hl" style="left:7px;top:20px">Headline here</h2>
  <span class="sub" style="left:7px;top:30px">Subheadline</span>
  <p class="txt" style="left:7px;top:37px;width:70px">Short body copy for the slide that runs across three tidy lines of text here.</p>
  <div class="bul" style="left:7px;top:56px"><b></b>Short bullet point text on one line</div>
  <div class="bul" style="left:7px;top:66px"><b></b>Short bullet point text on one line</div>
  <div class="bul" style="left:7px;top:76px"><b></b>Short bullet point text on one line</div>
  <div class="abs" style="left:88px;top:20px;width:30px;height:64px;background:var(--panel)"></div>
  <div class="abs" style="left:123px;top:20px;width:30px;height:64px;background:var(--panel)"></div>
  <div class="abs" style="left:158px;top:20px;width:30px;height:64px;background:var(--panel)"></div>
  <div class="ic red" style="left:92px;top:24px;width:22px;height:22px"></div>
  <div class="ic slate" style="left:127px;top:24px;width:22px;height:22px"></div>
  <div class="ic purple" style="left:162px;top:24px;width:22px;height:22px"></div>
  <span class="lbl" style="left:92px;top:52px">Headline</span>
  <span class="lbl" style="left:127px;top:52px">Headline</span>
  <span class="lbl" style="left:162px;top:52px">Headline</span>
  <div class="pg"></div>
</section>

<section class="slide" style="left:798px;top:16px">
  <span class="tag">Reach the right people, at the right time</span>
  <div class="mark"><span>RIVOPLEX</span><i></i></div>
  <svg class="abs" style="left:7px;top:30px" width="176" height="16" viewBox="0 0 176 16">
    <polygon points="0,0 38,0 44,8 38,16 0,16" fill="#e31e26"/>
    <polygon points="44,0 82,0 88,8 82,16 44,16 50,8" fill="#4b5261"/>
    <polygon points="88,0 126,0 132,8 126,16 88,16 94,8" fill="#5e9a3b"/>
    <polygon points="132,0 170,0 176,8 170,16 132,16 138,8" fill="#7b2682"/>
  </svg>
  <span class="lbl" style="left:7px;top:21px">Headline here</span>
  <span class="lbl" style="left:51px;top:21px;color:var(--slate)">Headline here</span>
  <span class="lbl" style="left:95px;top:21px;color:var(--green)">Headline here</span>
  <span class="lbl" style="left:139px;top:21px;color:var(--purple)">Headline here</span>
  <div class="abs" style="left:7px;top:50px;width:40px;height:36px;background:var(--panel)"></div>
  <div class="abs" style="left:51px;top:50px;width:40px;height:36px;background:var(--panel)"></div>
  <div class="abs" style="left:95px;top:50px;width:40px;height:36px;background:var(--panel)"></div>
  <div class="abs" style="left:139px;top:50px;width:40px;height:36px;background:var(--panel)"></div>
  <p class="txt" style="left:10px;top:55px;width:34px">Brief copy for this step goes here.</p>
  <p class="txt" style="left:54px;top:55px;width:34px">Brief copy for this step goes here.</p>
  <p class="txt" style="left:98px;top:55px;width:34px">Brief copy for this step goes here.</p>
  <p class="txt" style="left:142px;top:55px;width:34px">Brief copy for this step goes here.</p>
  <div class="pg"></div>
</section>

<section class="slide" style="left:996px;top:16px">
  <span class="tag">Reach the right people, at the right time</span>
  <div class="mark"><span>RIVOPLEX</span><i></i></div>
  <h2 class="hl" style="left:7px;top:20px">Headline here</h2>
  <span class="sub" style="left:7px;top:30px">Subheadline</span>
  <p class="txt" style="left:7px;top:37px;width:70px">Short body copy for the slide that runs across three tidy lines of text here.</p>
  <div class="bul" style="left:7px;top:60px"><b></b>Short bullet point text</div>
  <div class="bul" style="left:7px;top:70px"><b></b>Short bullet point text</div>
  <div class="bul" style="left:7px;top:80px"><b></b>Short bullet point text</div>
  <div class="ic o" style="left:92px;top:24px;width:14px;height:14px;border:.6px solid var(--line)"></div>
  <div class="ic o" style="left:140px;top:24px;width:14px;height:14px;border:.6px solid var(--line)"></div>
  <div class="ic o" style="left:92px;top:46px;width:14px;height:14px;border:.6px solid var(--line)"></div>
  <div class="ic o" style="left:140px;top:46px;width:14px;height:14px;border:.6px solid var(--line)"></div>
  <div class="ic o" style="left:92px;top:68px;width:14px;height:14px;border:.6px solid var(--line)"></div>
  <div class="ic o" style="left:140px;top:68px;width:14px;height:14px;border:.6px solid var(--line)"></div>
  <span class="lbl" style="left:109px;top:27px">Headline</span>
  <span class="lbl" style="left:157px;top:27px">Headline</span>
  <span class="lbl" style="left:109px;top:49px">Headline</span>
  <span class="lbl" style="left:157px;top:49px">Headline</span>
  <span class="lbl" style="left:109px;top:71px">Headline</span>
  <span class="lbl" style="left:157px;top:71px">Headline</span>
  <div class="pg"></div>
</section>

<!-- Row 2 -->
<section class="slide" style="left:406px;top:128px">
  <div class="photo dusk" style="left:0;top:0;width:190px;height:104px" role="img" aria-label="Hazy city skyline with tower photograph"></div>
  <div class="abs slate" style="left:0;top:0;width:190px;height:40px"></div>
  <span class="arrow-c" style="left:6px;top:10px;width:8px;height:8px"></span>
  <p class="band-title" style="left:18px;top:6px;font-size:6.5px;width:60px">How solid is your marketing data?</p>
  <p class="txt" style="left:18px;top:30px;color:#fff">Convert unstructured data into actionable intelligence</p>
  <div class="mark white" style="top:14px"><span>RIVOPLEX</span><i></i></div>
</section>

<section class="slide" style="left:602px;top:128px">
  <span class="tag">How solid is your marketing data?</span>
  <div class="mark"><span>RIVOPLEX</span><i></i></div>
  <div class="dot" style="left:7px;top:22px;width:7px;height:7px;border:.6px solid var(--mute)"></div>
  <div class="dot" style="left:7px;top:38px;width:7px;height:7px;border:.6px solid var(--mute)"></div>
  <div class="dot" style="left:7px;top:54px;width:7px;height:7px;border:.6px solid var(--mute)"></div>
  <div class="dot" style="left:7px;top:70px;width:7px;height:7px;border:.6px solid var(--mute)"></div>
  <span class="lbl" style="left:18px;top:21px;color:var(--ink)">Headline here</span>
  <span class="lbl" style="left:18px;top:37px;color:var(--ink)">Headline here</span>
  <span class="lbl" style="left:18px;top:53px;color:var(--ink)">Headline here</span>
  <span class="lbl" style="left:18px;top:69px;color:var(--ink)">Headline here</span>
  <p class="txt" style="left:18px;top:27px;width:70px">Short supporting copy for this point.</p>
  <p class="txt" style="left:18px;top:43px;width:70px">Short supporting copy for this point.</p>
  <p class="txt" style="left:18px;top:59px;width:70px">Short supporting copy for this point.</p>
  <p class="txt" style="left:18px;top:75px;width:70px">Short supporting copy for this point.</p>
  <div class="photo dusk" style="left:110px;top:20px;width:72px;height:62px" role="img" aria-label="City skyline with tower photograph"></div>
  <div class="pg"></div>
</section>

<section class="slide" style="left:798px;top:128px">
  <span class="tag">How solid is your marketing data?</span>
  <div class="mark"><span>RIVOPLEX</span><i></i></div>
  <div class="dot" style="left:66px;top:22px;width:58px;height:58px;background:var(--panel)"></div>
  <div class="dot red" style="left:80px;top:36px;width:30px;height:30px"></div>
  <span class="abs" style="left:82px;top:48px;font:600 4px 'Oswald',sans-serif;color:#fff;width:26px;text-align:center">RIVOPLEX</span>
  <div class="ic o" style="left:70px;top:30px;width:8px;height:8px;border:.5px solid var(--line);background:#fff"></div>
  <div class="ic o" style="left:112px;top:30px;width:8px;height:8px;border:.5px solid var(--line);background:#fff"></div>
  <div class="ic o" style="left:64px;top:47px;width:8px;height:8px;border:.5px solid var(--line);background:#fff"></div>
  <div class="ic o" style="left:118px;top:47px;width:8px;height:8px;border:.5px solid var(--line);background:#fff"></div>
  <div class="ic o" style="left:70px;top:64px;width:8px;height:8px;border:.5px solid var(--line);background:#fff"></div>
  <div class="ic o" style="left:112px;top:64px;width:8px;height:8px;border:.5px solid var(--line);background:#fff"></div>
  <span class="lbl" style="left:22px;top:30px">Headline here</span>
  <span class="lbl" style="left:14px;top:47px">Headline here</span>
  <span class="lbl" style="left:22px;top:64px">Headline here</span>
  <span class="lbl" style="left:132px;top:30px">Headline here</span>
  <span class="lbl" style="left:140px;top:47px">Headline here</span>
  <span class="lbl" style="left:132px;top:64px">Headline here</span>
  <div class="pg"></div>
</section>

<section class="slide" style="left:996px;top:128px">
  <span class="tag">How solid is your marketing data?</span>
  <div class="mark"><span>RIVOPLEX</span><i></i></div>
  <h2 class="hl" style="left:7px;top:20px">Headline here</h2>
  <span class="sub" style="left:7px;top:30px">Subheadline</span>
  <p class="txt" style="left:7px;top:37px;width:60px">Short body copy for the slide that runs across lines.</p>
  <div class="bul" style="left:7px;top:58px;width:58px"><b></b>Short bullet text</div>
  <div class="bul" style="left:7px;top:68px;width:58px"><b></b>Short bullet text</div>
  <div class="bul" style="left:7px;top:78px;width:58px"><b></b>Short bullet text</div>
  <table class="data" style="left:74px;top:20px;width:110px">
    <tr><th>Item</th><th>Text</th><th>Text</th><th>Text</th><th>Text</th><th>Text</th></tr>
    <tr><td>Text</td><td>20.5</td><td>20.5</td><td>20.5</td><td>20.5</td><td>20.5</td></tr>
    <tr><td>Text</td><td>20.5</td><td>20.5</td><td>20.5</td><td>20.5</td><td>20.5</td></tr>
    <tr><td>Text</td><td>20.5</td><td>20.5</td><td>20.5</td><td>20.5</td><td>20.5</td></tr>
    <tr><td>Text</td><td>20.5</td><td>20.5</td><td>20.5</td><td>20.5</td><td>20.5</td></tr>
    <tr><td>Text</td><td>20.5</td><td>20.5</td><td>20.5</td><td>20.5</td><td>20.5</td></tr>
    <tr><td>Text</td><td>20.5</td><td>20.5</td><td>20.5</td><td>20.5</td><td>20.5</td></tr>
    <tr><td>Text</td><td>20.5</td><td>20.5</td><td>20.5</td><td>20.5</td><td>20.5</td></tr>
    <tr class="total"><td>Total</td><td>123.0</td><td>123.0</td><td>123.0</td><td>123.0</td><td>123.0</td></tr>
  </table>
  <div class="pg"></div>
</section>

<!-- Row 3 -->
<section class="slide" style="left:11px;top:242px">
  <span class="tag">Reach the right people, at the right time</span>
  <div class="mark"><span>RIVOPLEX</span><i></i></div>
  <h2 class="hl" style="left:7px;top:22px">Headline here</h2>
  <span class="sub" style="left:7px;top:32px">Subheadline</span>
  <p class="txt" style="left:7px;top:39px;width:62px">Short body copy for the slide that runs across lines.</p>
  <div class="bul" style="left:7px;top:62px;width:60px"><b></b>Short bullet text</div>
  <div class="bul" style="left:7px;top:72px;width:60px"><b></b>Short bullet text</div>
  <div class="bul" style="left:7px;top:82px;width:60px"><b></b>Short bullet text</div>
  <svg class="abs" style="left:80px;top:20px" width="104" height="72" viewBox="0 0 104 72">
    <rect x="0" y="0" width="104" height="5" fill="#efefef"/>
    <rect x="6" y="1.5" width="2" height="2" fill="#4b5261"/><rect x="30" y="1.5" width="2" height="2" fill="#e31e26"/>
    <line x1="4" y1="64" x2="100" y2="64" stroke="#d9d9d9" stroke-width=".5"/>
    <rect x="10" y="44" width="5" height="20" fill="#e31e26"/><rect x="16" y="40" width="5" height="24" fill="#4b5261"/>
    <rect x="28" y="22" width="5" height="42" fill="#e31e26"/><rect x="34" y="16" width="5" height="48" fill="#4b5261"/>
    <rect x="46" y="14" width="5" height="50" fill="#e31e26"/><rect x="52" y="18" width="5" height="46" fill="#4b5261"/>
    <rect x="64" y="38" width="5" height="26" fill="#e31e26"/><rect x="70" y="36" width="5" height="28" fill="#4b5261"/>
    <rect x="82" y="40" width="5" height="24" fill="#e31e26"/><rect x="88" y="36" width="5" height="28" fill="#4b5261"/>
  </svg>
  <div class="pg"></div>
</section>

<section class="slide" style="left:208px;top:242px">
  <span class="tag" style="font:500 5px 'Oswald',sans-serif;color:var(--ink)">About us</span>
  <div class="mark"><span>RIVOPLEX</span><i></i></div>
  <div class="abs" style="left:0;top:38px;width:190px;height:44px;background:var(--panel)"></div>
  <div class="abs" style="left:10px;top:22px;width:32px;height:32px;border:.6px solid var(--red);background:#fff"></div>
  <div class="abs" style="left:55px;top:22px;width:32px;height:32px;border:.6px solid var(--red);background:#fff"></div>
  <div class="abs" style="left:100px;top:22px;width:32px;height:32px;border:.6px solid var(--red);background:#fff"></div>
  <div class="abs" style="left:145px;top:22px;width:32px;height:32px;border:.6px solid var(--red);background:#fff"></div>
  <span class="lbl" style="left:10px;top:58px;color:var(--ink)">Name Surname</span>
  <span class="lbl" style="left:55px;top:58px;color:var(--ink)">Name Surname</span>
  <span class="lbl" style="left:100px;top:58px;color:var(--ink)">Name Surname</span>
  <span class="lbl" style="left:145px;top:58px;color:var(--ink)">Name Surname</span>
  <p class="txt" style="left:10px;top:64px">Position title</p>
  <p class="txt" style="left:55px;top:64px">Position title</p>
  <p class="txt" style="left:100px;top:64px">Position title</p>
  <p class="txt" style="left:145px;top:64px">Position title</p>
  <div class="pg"></div>
</section>

<section class="slide" style="left:406px;top:242px">
  <span class="tag">How solid is your marketing data?</span>
  <div class="mark"><span>RIVOPLEX</span><i></i></div>
  <h2 class="hl" style="left:7px;top:22px">Headline here</h2>
  <span class="sub" style="left:7px;top:32px">Subheadline</span>
  <p class="txt" style="left:7px;top:39px;width:78px">Short body copy for the slide that runs across three tidy lines of text here.</p>
  <div class="bul" style="left:7px;top:62px"><b></b>Short bullet point text</div>
  <div class="bul" style="left:7px;top:72px"><b></b>Short bullet point text</div>
  <div class="bul" style="left:7px;top:82px"><b></b>Short bullet point text</div>
  <div class="abs" style="left:104px;top:24px;width:80px;height:14px;background:var(--panel)"></div>
  <div class="abs" style="left:104px;top:44px;width:80px;height:14px;background:var(--panel)"></div>
  <div class="abs" style="left:104px;top:64px;width:80px;height:14px;background:var(--panel)"></div>
  <div class="ic red" style="left:98px;top:21px;width:19px;height:19px"></div>
  <div class="ic slate" style="left:98px;top:41px;width:19px;height:19px"></div>
  <div class="ic green" style="left:98px;top:61px;width:19px;height:19px"></div>
  <span class="lbl" style="left:122px;top:26px">Headline here</span>
  <span class="lbl" style="left:122px;top:46px">Headline here</span>
  <span class="lbl" style="left:122px;top:66px">Headline here</span>
  <p class="txt" style="left:122px;top:31px">Short supporting copy</p>
  <p class="txt" style="left:122px;top:51px">Short supporting copy</p>
  <p class="txt" style="left:122px;top:71px">Short supporting copy</p>
  <div class="pg"></div>
</section>

<section class="slide" style="left:602px;top:242px">
  <div class="photo night" style="left:0;top:0;width:190px;height:104px" role="img" aria-label="City skyline at evening photograph"></div>
  <div class="abs green" style="left:0;top:0;width:190px;height:42px"></div>
  <span class="arrow-c" style="left:6px;top:10px;width:8px;height:8px"></span>
  <p class="band-title" style="left:18px;top:6px;font-size:6.5px;width:80px">Inbound &amp; outbound call centres</p>
  <p class="txt" style="left:18px;top:28px;color:#fff;width:90px">Whether your aim is to acquire new customers or grow their value.</p>
  <div class="mark white" style="top:14px"><span>RIVOPLEX</span><i></i></div>
</section>

<section class="slide" style="left:798px;top:242px">
  <span class="tag">Inbound &amp; outbound call centres</span>
  <div class="mark"><span>RIVOPLEX</span><i></i></div>
  <div class="abs" style="left:0;top:36px;width:190px;height:24px;background:var(--panel)"></div>
  <div class="ic red" style="left:12px;top:20px;width:10px;height:10px"></div>
  <div class="ic slate" style="left:72px;top:20px;width:10px;height:10px"></div>
  <div class="ic green" style="left:132px;top:20px;width:10px;height:10px"></div>
  <div class="ic red" style="left:12px;top:43px;width:10px;height:10px"></div>
  <div class="ic slate" style="left:72px;top:43px;width:10px;height:10px"></div>
  <div class="ic green" style="left:132px;top:43px;width:10px;height:10px"></div>
  <div class="ic red" style="left:12px;top:66px;width:10px;height:10px"></div>
  <div class="ic slate" style="left:72px;top:66px;width:10px;height:10px"></div>
  <div class="ic green" style="left:132px;top:66px;width:10px;height:10px"></div>
  <p class="txt" style="left:26px;top:20px;width:42px">Short copy for this item goes here.</p>
  <p class="txt" style="left:86px;top:20px;width:42px">Short copy for this item goes here.</p>
  <p class="txt" style="left:146px;top:20px;width:40px">Short copy for this item goes here.</p>
  <p class="txt" style="left:26px;top:43px;width:42px">Short copy for this item goes here.</p>
  <p class="txt" style="left:86px;top:43px;width:42px">Short copy for this item goes here.</p>
  <p class="txt" style="left:146px;top:43px;width:40px">Short copy for this item goes here.</p>
  <p class="txt" style="left:26px;top:66px;width:42px">Short copy for this item goes here.</p>
  <p class="txt" style="left:86px;top:66px;width:42px">Short copy for this item goes here.</p>
  <p class="txt" style="left:146px;top:66px;width:40px">Short copy for this item goes here.</p>
  <div class="pg"></div>
</section>

<section class="slide" style="left:996px;top:242px">
  <span class="tag">Inbound &amp; outbound call centres</span>
  <div class="mark"><span>RIVOPLEX</span><i></i></div>
  <span class="lbl" style="left:7px;top:20px;color:var(--ink)">World map</span>
  <div class="abs" role="img" aria-label="Grey world map with red location pins across Asia Pacific" style="left:7px;top:30px;width:118px;height:58px;background:linear-gradient(135deg,#e6e6e6,#cfcfcf)"></div>
  <div class="ic red" style="left:134px;top:20px;width:10px;height:10px"></div>
  <div class="ic slate" style="left:134px;top:38px;width:10px;height:10px"></div>
  <div class="ic green" style="left:134px;top:56px;width:10px;height:10px"></div>
  <div class="ic purple" style="left:134px;top:74px;width:10px;height:10px"></div>
  <span class="lbl" style="left:148px;top:20px">Headline here</span>
  <span class="lbl" style="left:148px;top:38px">Headline here</span>
  <span class="lbl" style="left:148px;top:56px">Headline here</span>
  <span class="lbl" style="left:148px;top:74px">Headline here</span>
  <p class="txt" style="left:148px;top:25px">Short copy line</p>
  <p class="txt" style="left:148px;top:43px">Short copy line</p>
  <p class="txt" style="left:148px;top:61px">Short copy line</p>
  <p class="txt" style="left:148px;top:79px">Short copy line</p>
  <div class="pg"></div>
</section>

<!-- Row 4 -->
<section class="slide" style="left:11px;top:356px">
  <span class="tag">Inbound &amp; outbound call centres</span>
  <div class="mark"><span>RIVOPLEX</span><i></i></div>
  <div class="abs" style="left:10px;top:18px;width:36px;height:30px;background:var(--panel)"></div>
  <div class="abs" style="left:54px;top:18px;width:36px;height:30px;background:var(--panel)"></div>
  <div class="abs" style="left:98px;top:18px;width:36px;height:30px;background:var(--panel)"></div>
  <div class="abs" style="left:142px;top:18px;width:36px;height:30px;background:var(--panel)"></div>
  <span class="lbl" style="left:14px;top:40px">Headline here</span>
  <span class="lbl" style="left:58px;top:40px;color:var(--slate)">Headline here</span>
  <span class="lbl" style="left:102px;top:40px;color:var(--green)">Headline here</span>
  <span class="lbl" style="left:146px;top:40px;color:var(--purple)">Headline here</span>
  <div class="ring c-red" style="left:14px;top:56px;width:28px;height:28px"></div>
  <div class="ring c-slate" style="left:58px;top:56px;width:28px;height:28px"></div>
  <div class="ring c-green" style="left:102px;top:56px;width:28px;height:28px"></div>
  <div class="ring c-purple" style="left:146px;top:56px;width:28px;height:28px"></div>
  <div class="pg"></div>
</section>

<section class="slide" style="left:208px;top:356px">
  <span class="tag">Inbound &amp; outbound call centres</span>
  <div class="mark"><span>RIVOPLEX</span><i></i></div>
  <div class="abs" style="left:14px;top:22px;width:162px;height:26px;background:var(--panel);border-radius:13px"></div>
  <div class="abs" style="left:14px;top:54px;width:162px;height:26px;background:var(--panel);border-radius:13px"></div>
  <div class="ic red" style="left:70px;top:24px;width:22px;height:22px"></div>
  <div class="ic slate" style="left:98px;top:24px;width:22px;height:22px"></div>
  <div class="ic green" style="left:70px;top:56px;width:22px;height:22px"></div>
  <div class="ic purple" style="left:98px;top:56px;width:22px;height:22px"></div>
  <span class="lbl" style="left:28px;top:27px;color:var(--red)">Headline here</span>
  <span class="lbl" style="left:126px;top:27px;color:var(--ink)">Headline here</span>
  <span class="lbl" style="left:28px;top:59px;color:var(--green)">Headline here</span>
  <span class="lbl" style="left:126px;top:59px;color:var(--ink)">Headline here</span>
  <p class="txt" style="left:28px;top:33px;width:40px">Short copy for this item.</p>
  <p class="txt" style="left:126px;top:33px;width:40px">Short copy for this item.</p>
  <p class="txt" style="left:28px;top:65px;width:40px">Short copy for this item.</p>
  <p class="txt" style="left:126px;top:65px;width:40px">Short copy for this item.</p>
  <div class="dot" style="left:6px;top:20px;width:8px;height:8px;border:.6px solid var(--red);background:#fff;font:600 4px/7px 'Oswald',sans-serif;text-align:center;color:var(--red)">1</div>
  <div class="dot" style="left:176px;top:20px;width:8px;height:8px;border:.6px solid var(--slate);background:#fff;font:600 4px/7px 'Oswald',sans-serif;text-align:center;color:var(--slate)">3</div>
  <div class="dot" style="left:6px;top:74px;width:8px;height:8px;border:.6px solid var(--green);background:#fff;font:600 4px/7px 'Oswald',sans-serif;text-align:center;color:var(--green)">2</div>
  <div class="dot" style="left:176px;top:74px;width:8px;height:8px;border:.6px solid var(--purple);background:#fff;font:600 4px/7px 'Oswald',sans-serif;text-align:center;color:var(--purple)">4</div>
  <div class="pg"></div>
</section>

<section class="slide" style="left:406px;top:356px">
  <div class="photo night" style="left:0;top:0;width:190px;height:104px" role="img" aria-label="Twin towers skyline at night photograph"></div>
  <div class="abs purple" style="left:0;top:0;width:190px;height:42px"></div>
  <span class="arrow-c" style="left:6px;top:10px;width:8px;height:8px"></span>
  <p class="band-title" style="left:18px;top:5px;font-size:6.5px;width:80px">Better data, better target, better results</p>
  <p class="txt" style="left:18px;top:28px;color:#fff;width:96px">Delve into the behaviour of your most receptive and profitable customers.</p>
  <div class="mark white" style="top:14px"><span>RIVOPLEX</span><i></i></div>
</section>

<section class="slide" style="left:602px;top:356px">
  <span class="tag">Better data, better target, better results</span>
  <div class="mark"><span>RIVOPLEX</span><i></i></div>
  <div class="ic red" style="left:12px;top:24px;width:28px;height:28px;box-shadow:0 0 0 2px #fff,0 0 0 2.6px var(--line)"></div>
  <div class="ic slate" style="left:58px;top:24px;width:28px;height:28px;box-shadow:0 0 0 2px #fff,0 0 0 2.6px var(--line)"></div>
  <div class="ic green" style="left:104px;top:24px;width:28px;height:28px;box-shadow:0 0 0 2px #fff,0 0 0 2.6px var(--line)"></div>
  <div class="ic purple" style="left:150px;top:24px;width:28px;height:28px;box-shadow:0 0 0 2px #fff,0 0 0 2.6px var(--line)"></div>
  <svg class="abs" style="left:42px;top:34px" width="140" height="8" viewBox="0 0 140 8"><g fill="none" stroke="#8a8a8a" stroke-width=".8"><polyline points="8,1 12,4 8,7"/><polyline points="54,1 58,4 54,7"/><polyline points="100,1 104,4 100,7"/></g></svg>
  <span class="lbl" style="left:12px;top:58px">Headline here</span>
  <span class="lbl" style="left:58px;top:58px;color:var(--slate)">Headline here</span>
  <span class="lbl" style="left:104px;top:58px;color:var(--green)">Headline here</span>
  <span class="lbl" style="left:150px;top:58px;color:var(--purple)">Headline here</span>
  <p class="txt" style="left:12px;top:64px;width:34px">Short copy for this step goes here.</p>
  <p class="txt" style="left:58px;top:64px;width:34px">Short copy for this step goes here.</p>
  <p class="txt" style="left:104px;top:64px;width:34px">Short copy for this step goes here.</p>
  <p class="txt" style="left:150px;top:64px;width:34px">Short copy for this step goes here.</p>
  <div class="pg"></div>
</section>

<!-- Closing slide -->
<section class="slide close">
  <div class="photo night" style="left:0;top:0;width:387px;height:128px" role="img" aria-label="Waterfront skyline with lotus-shaped museum at dusk photograph"></div>
  <div class="close-mark"><span>RIVOPLEX</span><i></i></div>
  <div class="foot">
    <h2 style="left:28px;top:14px">ABOUT US</h2>
    <p>RivoPlex is the primary source of market intelligence focused on identifying business opportunities and key decision makers throughout Asia Pacific Region. We provide access to over 3.5 million decision makers across 1.5 million profiled organizations in 23 Asia Pacific countries. With our local presence in 8 countries, we provide tailored target marketing programs in Asia Pacific Region.</p>
    <h2 style="left:288px;top:14px;font-size:8px">CONTACT US</h2>
    <div class="contact">
      <div>+1 (555) 014-2207</div>
      <div>hello@rivoplex.com</div>
      <div>www.rivoplex.com</div>
    </div>
    <div class="social"><span></span><span></span><span></span><span></span></div>
  </div>
</section>

<!-- Row 5 -->
<section class="slide" style="left:11px;top:470px">
  <div class="photo night" style="left:0;top:0;width:88px;height:68px" role="img" aria-label="City skyline at night photograph"></div>
  <div class="photo night" style="left:88px;top:68px;width:102px;height:36px" role="img" aria-label="Waterfront skyline at dusk photograph"></div>
  <div class="abs red" style="left:0;top:68px;width:88px;height:2px"></div>
  <h2 class="hl" style="left:96px;top:12px">Headline here</h2>
  <span class="sub" style="left:96px;top:22px">Subheadline</span>
  <div class="bul" style="left:96px;top:30px;width:42px"><b></b>Short bullet text</div>
  <div class="bul" style="left:96px;top:40px;width:42px"><b></b>Short bullet text</div>
  <div class="bul" style="left:96px;top:50px;width:42px"><b></b>Short bullet text</div>
  <div class="bul" style="left:142px;top:30px;width:42px"><b></b>Short bullet text</div>
  <div class="bul" style="left:142px;top:40px;width:42px"><b></b>Short bullet text</div>
  <div class="bul" style="left:142px;top:50px;width:42px"><b></b>Short bullet text</div>
  <h2 class="hl" style="left:6px;top:76px;font-size:6px">Headline here</h2>
  <span class="sub" style="left:6px;top:84px">Subheadline</span>
  <div class="bul" style="left:46px;top:74px;width:40px"><b></b>Short bullet</div>
  <div class="bul" style="left:46px;top:83px;width:40px"><b></b>Short bullet</div>
  <div class="bul" style="left:46px;top:92px;width:40px"><b></b>Short bullet</div>
</section>

<section class="slide" style="left:208px;top:470px">
  <span class="tag">Better data, better target, better results</span>
  <div class="mark"><span>RIVOPLEX</span><i></i></div>
  <svg class="abs" style="left:8px;top:18px" width="176" height="36" viewBox="0 0 176 36">
    <g fill="none" stroke-width="3.5">
      <circle cx="20" cy="18" r="14" stroke="#efefef"/><circle cx="20" cy="18" r="14" stroke="#e31e26" stroke-dasharray="57.2 88" transform="rotate(-90 20 18)"/>
      <circle cx="65" cy="18" r="14" stroke="#efefef"/><circle cx="65" cy="18" r="14" stroke="#4b5261" stroke-dasharray="61.6 88" transform="rotate(-90 65 18)"/>
      <circle cx="110" cy="18" r="14" stroke="#efefef"/><circle cx="110" cy="18" r="14" stroke="#5e9a3b" stroke-dasharray="52.8 88" transform="rotate(-90 110 18)"/>
      <circle cx="155" cy="18" r="14" stroke="#efefef"/><circle cx="155" cy="18" r="14" stroke="#7b2682" stroke-dasharray="26.4 88" transform="rotate(-90 155 18)"/>
    </g>
    <g font-family="Oswald,sans-serif" font-size="7" font-weight="500" text-anchor="middle">
      <text x="20" y="20.5" fill="#e31e26">65%</text><text x="65" y="20.5" fill="#4b5261">70%</text>
      <text x="110" y="20.5" fill="#5e9a3b">60%</text><text x="155" y="20.5" fill="#7b2682">30%</text>
    </g>
  </svg>
  <div class="abs red" style="left:10px;top:60px;width:36px;height:6px"></div>
  <div class="abs slate" style="left:55px;top:60px;width:36px;height:6px"></div>
  <div class="abs green" style="left:100px;top:60px;width:36px;height:6px"></div>
  <div class="abs purple" style="left:145px;top:60px;width:36px;height:6px"></div>
  <span class="lbl" style="left:14px;top:60.5px;color:#fff">Headline here</span>
  <span class="lbl" style="left:59px;top:60.5px;color:#fff">Headline here</span>
  <span class="lbl" style="left:104px;top:60.5px;color:#fff">Headline here</span>
  <span class="lbl" style="left:149px;top:60.5px;color:#fff">Headline here</span>
  <p class="txt" style="left:10px;top:70px;width:36px">Short copy for this value here.</p>
  <p class="txt" style="left:55px;top:70px;width:36px">Short copy for this value here.</p>
  <p class="txt" style="left:100px;top:70px;width:36px">Short copy for this value here.</p>
  <p class="txt" style="left:145px;top:70px;width:36px">Short copy for this value here.</p>
  <div class="pg"></div>
</section>

<section class="slide" style="left:406px;top:470px">
  <span class="tag">Better data, better target, better results</span>
  <div class="mark"><span>RIVOPLEX</span><i></i></div>
  <svg class="abs" style="left:8px;top:16px" width="176" height="40" viewBox="0 0 176 40">
    <g fill="none" stroke-width="1.5">
      <circle cx="20" cy="20" r="14" stroke="#e6e6e6"/><circle cx="20" cy="20" r="14" stroke="#e31e26" stroke-dasharray="22 88" transform="rotate(-90 20 20)"/>
      <circle cx="65" cy="20" r="14" stroke="#e6e6e6"/><circle cx="65" cy="20" r="14" stroke="#4b5261" stroke-dasharray="57 88" transform="rotate(-90 65 20)"/>
      <circle cx="110" cy="20" r="14" stroke="#e6e6e6"/><circle cx="110" cy="20" r="14" stroke="#5e9a3b" stroke-dasharray="57 88" transform="rotate(-90 110 20)"/>
      <circle cx="155" cy="20" r="14" stroke="#e6e6e6"/><circle cx="155" cy="20" r="14" stroke="#7b2682" stroke-dasharray="57 88" transform="rotate(-90 155 20)"/>
    </g>
    <circle cx="20" cy="20" r="9" fill="#f3f3f3"/><circle cx="65" cy="20" r="9" fill="#f3f3f3"/>
    <circle cx="110" cy="20" r="9" fill="#f3f3f3"/><circle cx="155" cy="20" r="9" fill="#f3f3f3"/>
    <g fill="none" stroke-width=".8"><circle cx="20" cy="20" r="3" stroke="#e31e26"/><circle cx="65" cy="20" r="3" stroke="#4b5261"/><circle cx="110" cy="20" r="3" stroke="#5e9a3b"/><circle cx="155" cy="20" r="3" stroke="#7b2682"/></g>
    <g font-family="Oswald,sans-serif" font-size="4.5" fill="#8a8a8a">
      <text x="28" y="6">25%</text><text x="1" y="32">25%</text><text x="73" y="6">20%</text><text x="46" y="32">65%</text>
      <text x="118" y="6">20%</text><text x="91" y="32">65%</text><text x="163" y="6">20%</text><text x="136" y="32">65%</text>
    </g>
  </svg>
  <span class="lbl" style="left:14px;top:62px;color:var(--ink)">Headline here</span>
  <span class="lbl" style="left:59px;top:62px;color:var(--ink)">Headline here</span>
  <span class="lbl" style="left:104px;top:62px;color:var(--ink)">Headline here</span>
  <span class="lbl" style="left:149px;top:62px;color:var(--ink)">Headline here</span>
  <p class="txt" style="left:10px;top:70px;width:36px">Short copy for this value here.</p>
  <p class="txt" style="left:55px;top:70px;width:36px">Short copy for this value here.</p>
  <p class="txt" style="left:100px;top:70px;width:36px">Short copy for this value here.</p>
  <p class="txt" style="left:145px;top:70px;width:36px">Short copy for this value here.</p>
  <div class="pg"></div>
</section>

<section class="slide" style="left:602px;top:470px">
  <div class="photo dusk" style="left:0;top:0;width:48px;height:52px" role="img" aria-label="City tower skyline photograph"></div>
  <div class="photo day" style="left:96px;top:0;width:48px;height:52px" role="img" aria-label="Daytime skyline photograph"></div>
  <div class="photo night" style="left:48px;top:52px;width:48px;height:52px" role="img" aria-label="Twin towers at night photograph"></div>
  <div class="photo night" style="left:144px;top:52px;width:46px;height:52px" role="img" aria-label="Harbour skyline at night photograph"></div>
  <div class="abs red" style="left:48px;top:0;width:48px;height:52px"></div>
  <div class="abs red" style="left:144px;top:0;width:46px;height:52px"></div>
  <div class="abs red" style="left:0;top:52px;width:48px;height:52px"></div>
  <div class="abs red" style="left:96px;top:52px;width:48px;height:52px"></div>
  <span class="abs slate" style="left:52px;top:6px;padding:1px 2px;font:600 3.6px 'Oswald',sans-serif;color:#fff">HEADLINE HERE</span>
  <span class="abs slate" style="left:148px;top:6px;padding:1px 2px;font:600 3.6px 'Oswald',sans-serif;color:#fff">HEADLINE HERE</span>
  <span class="abs slate" style="left:4px;top:70px;padding:1px 2px;font:600 3.6px 'Oswald',sans-serif;color:#fff">HEADLINE HERE</span>
  <span class="abs slate" style="left:100px;top:58px;padding:1px 2px;font:600 3.6px 'Oswald',sans-serif;color:#fff">HEADLINE HERE</span>
  <p class="txt" style="left:52px;top:14px;width:40px;color:#fff">Short copy for the panel goes here now.</p>
  <p class="txt" style="left:148px;top:14px;width:38px;color:#fff">Short copy for the panel goes here now.</p>
  <p class="txt" style="left:4px;top:78px;width:40px;color:#fff">Short copy for the panel goes here now.</p>
  <p class="txt" style="left:100px;top:66px;width:40px;color:#fff">Short copy for the panel goes here now.</p>
  <div class="mark white" style="left:4px;right:auto;top:58px;font-size:5px"><span>RIVOPLEX</span><i></i></div>
</section>

</body>
</html>
```